Career Drop Down Layout on CopperTrailhead.com Quiz Results

We want to redesign the career drop down view after people take the career finder quiz at CopperTrailhead.com. After you take the quiz (feel free to take it yourself), you get a results page. On the left hand navigation bar, go to Career Matches (in green). When you open one of your career matches, we want people to see lots of great information about the job. We need help figuring out how to display the information. The information we want to display is the following:

1) name of job
2) WERQ description
3) Link to the Werq info
4) Match dial
5) Rising Outlook image
6) a video about the job
7) Average salary
8) Minimum Qualifications
9) Top Tips
10) Recommended Programs
11) Jobs in their area - by Hireloop Finder

I put screen shots of what we have now and a mock-up of the new elements in the brief. It can look anyway you think will be good. I'm not tied to the mock-up at all.

To see how your design will look live on the web do the following:

1) Login at: https://www.coppertrailhead.com/survey/login (or take the quiz yourself to see your own results)
2) Enter Email address: marla.voss@copperventure.org
3) Enter Password: 123456
4) See results summary - Click on Career Matches from the left navigation bar
5) See the career matches, when you click the arrow on the right side of each career match it will display the new page you are designing for each career with info from a database.

Thanks, Marla

Target Market(s)

Young people looking for jobs

Number of Pages Required

1 page

Requirements
Must have
• The layout of how all the information will look nicely on a computer screen. It can scroll down more vertically if necessary.

The color scheme and text must match the existing site since this page will be embedded in our site. I attached our design guide.
Nice to have
• I'd like to see a very easy to scan, organized way to display a lot of job information.

```html
<!DOCTYPE html>
<html lang="en">
<head>
<meta charset="utf-8">
<title>Career Matches – Copper Trailhead</title>
<link href="https://fonts.googleapis.com/css2?family=Montserrat:wght@400;500;600&family=Roboto:wght@400;500&display=swap" rel="stylesheet">
<style>
:root{
  --purple:#4c43a0;
  --purple-dark:#302b6e;
  --heading:#4a3aa6;
  --green:#77c043;
  --text:#222;
  --muted:#666;
  --page:#f5f5f7;
  --panel:#f4f4f5;
  --line:#e4e4e8;
  --link:#2f57d8;
}
*{box-sizing:border-box;margin:0;padding:0}
html,body{width:1200px;height:919px;overflow:hidden}
body{font-family:"Montserrat",sans-serif;background:var(--page);color:var(--text);position:relative}
.abs{position:absolute}

/* top bar */
.topbar{left:0;top:0;width:1200px;height:50px;background:#fff;border-bottom:1px solid #eee}
.brand{left:36px;top:16px;font-size:13px;font-weight:600;color:var(--green);display:flex;align-items:center;gap:6px}
.brand .dot{width:9px;height:9px;border-radius:50%;background:var(--green)}
.nav{left:462px;top:18px;display:flex;gap:25px;font-size:11px;color:#333}
.nav .caret::after{content:"";display:inline-block;margin-left:3px;border:3px solid transparent;border-top:4px solid #333;vertical-align:-1px}
.search{left:744px;top:13px;width:222px;height:26px;border-radius:13px;background:#f2f2f4;border:1px solid #e6e6ea;font:10px "Roboto",sans-serif;color:#999;padding:7px 12px}
.search svg{position:absolute;right:8px;top:6px}
.lang{left:990px;top:18px;font-size:11px;font-weight:500;display:flex;align-items:center;gap:4px}
.flag{width:8px;height:8px;border-radius:50%;background:linear-gradient(#c33 50%,#35a 50%)}
.bell{left:1050px;top:16px}
.badge{left:1057px;top:13px;width:9px;height:9px;border-radius:50%;background:var(--green);color:#fff;font-size:6px;text-align:center;line-height:9px}
.user{left:1090px;top:14px;display:flex;align-items:center;gap:8px;font-size:11px;font-weight:600}
.avatar{width:22px;height:22px;border-radius:50%;background:linear-gradient(#9a8b7c,#5f5045)}

/* sidebar */
.sidebar{left:0;top:51px;width:166px;height:868px;background:var(--purple)}
.sidebar .who{height:81px;background:#4a409a;text-align:center;color:#fff;font-size:12px;font-weight:600;padding-top:14px}
.sidebar .who .avatar{width:37px;height:37px;margin:7px auto 0}
.menu{list-style:none;margin-top:12px}
.menu li{height:33px;line-height:33px;padding-left:35px;color:#fff;font-size:10.5px}
.menu li.active{background:var(--green)}

/* heading area */
.title{left:166px;width:1034px;top:86px;text-align:center;font-size:29px;font-weight:600;color:var(--heading)}
.title span{color:var(--green)}
.rate{left:401px;top:143px;display:flex;align-items:center;font:500 11.5px "Montserrat",sans-serif}
.rate .lbl{margin-right:18px}
.rate .opt{display:flex;align-items:center;gap:8px;margin-right:14px;font:500 10px "Roboto",sans-serif;color:#444}
.ic{width:28px;height:28px;border-radius:50%;background:#fff;box-shadow:0 1px 4px rgba(0,0,0,.12);display:flex;align-items:center;justify-content:center}
.hint{left:166px;width:1034px;top:180px;text-align:center;font:10px "Roboto",sans-serif;color:#444}

/* card */
.card{left:219px;top:220px;width:928px;height:591px;background:#fff;box-shadow:0 1px 6px rgba(0,0,0,.08)}
.fav{left:0;width:928px;top:23px;text-align:center;font-size:23px;font-weight:600;color:var(--heading)}
.jobbar{left:32px;top:71px;width:863px;height:39px;border-radius:20px;background:#f1f1f3;display:flex;align-items:center;padding-left:22px}
.jobbar .ic{margin-right:10px}
.jobbar .name{margin-left:14px;font-size:12.5px;font-weight:500}
.jobbar .arrow{position:absolute;right:22px;top:17px;border:4px solid transparent;border-top:5px solid #222}

.col{top:148px;height:336px;background:var(--panel);border:1px solid var(--line);border-radius:4px}
.c1{left:32px;width:279px;padding:18px 10px 18px 18px}
.c2{left:337px;width:254px;text-align:center}
.c3{left:615px;width:279px;padding:14px 10px 14px 18px}
.h3{font-size:14.5px;font-weight:500;color:var(--heading)}
.desc{margin-top:13px;font-size:10px;line-height:18.8px;color:#555}
.btn{display:block;width:229px;height:34px;margin-left:6px;border-radius:2px;color:#fff;font-size:10.5px;font-weight:600;text-align:center;line-height:34px}
.btn.purple{background:var(--purple);margin-top:28px}
.btn.green{background:var(--green);margin-top:10px}

.gauge{margin-top:16px}
.match{font:10px "Roboto",sans-serif;color:#555;margin-top:2px}
.c2 .h3{margin-top:12px}
.val{font-size:12px;font-weight:500}
.outlook{margin-top:13px;font-size:12px;font-weight:600;color:#f0a020;display:flex;justify-content:center;align-items:center;gap:3px}
.outlook i{width:10px;height:10px;border-radius:50%;background:#f6c400}
.video{margin:12px auto 0;width:228px;height:93px;background:linear-gradient(120deg,#d9cdb8,#7e6f5f 55%,#4a4a50);position:relative}
.video .play{position:absolute;left:101px;top:33px}
.c2 .h3.q{margin-top:15px}

.tips{margin-top:12px;list-style:none;font-size:10px;line-height:17px;color:#555}
.tips li{display:flex;gap:10px;margin-bottom:4px}
.tips b{color:#222}
.c3 .h3.p{margin-top:8px}
.prog{display:flex;align-items:center;gap:16px;margin-top:12px;font-size:10.5px}
.prog .ic{width:38px;height:38px}
.prog a{color:var(--link);text-decoration:underline}
.prog+.prog{margin-top:9px}
.btn.wide{margin:18px 0 0 6px}

.area{left:0;width:928px;top:532px;display:flex;justify-content:center;align-items:center;gap:12px;font-size:11.5px;font-weight:500}
.area .partner{font-size:14px;font-weight:600;color:#333;display:flex;align-items:center;gap:5px}
.area .partner i{width:9px;height:9px;background:var(--green)}

/* footer */
.footer{left:166px;top:877px;width:1034px;height:42px;background:var(--purple-dark);color:#fff;font-size:11.5px}
.footer .links{position:absolute;left:39px;top:13px}
.footer .copy{position:absolute;left:699px;top:14px;font-size:11px}
.footer .code{position:absolute;left:989px;top:14px;font-size:11px}
</style>
</head>
<body>

<header class="abs topbar">
  <div class="abs brand"><span class="dot"></span>Copper Trailhead</div>
  <nav class="abs nav"><span>Home</span><span class="caret">My Results</span><span class="caret">Services</span></nav>
  <div class="abs search">Search
    <svg width="12" height="12" viewBox="0 0 12 12"><circle cx="5" cy="5" r="3.8" fill="none" stroke="#111" stroke-width="1.6"/><line x1="8" y1="8" x2="11" y2="11" stroke="#111" stroke-width="1.6"/></svg>
  </div>
  <div class="abs lang"><span class="flag"></span>Eng ⌄</div>
  <svg class="abs bell" width="14" height="14" viewBox="0 0 14 14"><path d="M7 1a4 4 0 0 0-4 4v4l-1.5 2h11L11 9V5a4 4 0 0 0-4-4z" fill="#111"/><circle cx="7" cy="12.5" r="1.3" fill="#111"/></svg>
  <div class="abs badge">3</div>
  <div class="abs user"><span class="avatar" role="img" aria-label="Profile photo"></span>Marla's ⌄</div>
</header>

<aside class="abs sidebar">
  <div class="who">Marla's Results<div class="avatar" role="img" aria-label="Profile photo"></div></div>
  <ul class="menu">
    <li>Results Summary</li>
    <li>What Motivates You</li>
    <li>Your DISC Profile</li>
    <li class="active">Career Matches ▾</li>
    <li>Maximize My Results</li>
    <li>Communication Tips</li>
    <li>Reflections and Goals</li>
    <li>Resources</li>
  </ul>
</aside>

<h1 class="abs title"><span>Career</span> Matches</h1>
<div class="abs rate">
  <span class="lbl">Rate as many jobs as you can:</span>
  <span class="opt"><span class="ic"><svg width="13" height="13" viewBox="0 0 14 14"><path d="M2 6h2v7H2zM5 6l3-5c1 0 1.5 1 1 2.5L8.5 5H12l-1 8H5z" fill="none" stroke="#77c043" stroke-width="1.1"/></svg></span>Send to favorites</span>
  <span class="opt"><span class="ic"><svg width="13" height="13" viewBox="0 0 14 14"><path d="M3 7V3h2v4M5 5V2h2v5M7 4V2h2v5M9 5h2v4l-2 4H5L3 9V7" fill="none" stroke="#4c43a0" stroke-width="1.1"/></svg></span>Not sure</span>
  <span class="opt"><span class="ic"><svg width="13" height="13" viewBox="0 0 14 14"><path d="M2 1h2v7H2zM5 8l3 5c1 0 1.5-1 1-2.5L8.5 9H12l-1-8H5z" fill="none" stroke="#e02424" stroke-width="1.1"/></svg></span>No way - send to archive!</span>
</div>
<p class="abs hint">Click on each category for in-depth descriptions, resources, education options, and tips.</p>

<main class="abs card">
  <h2 class="abs fav">Favorites</h2>
  <div class="abs jobbar">
    <span class="ic"><svg width="13" height="13" viewBox="0 0 14 14"><path d="M2 6h2v7H2zM5 6l3-5c1 0 1.5 1 1 2.5L8.5 5H12l-1 8H5z" fill="none" stroke="#77c043" stroke-width="1.1"/></svg></span>
    <span class="ic"><svg width="13" height="13" viewBox="0 0 14 14"><path d="M3 7V3h2v4M5 5V2h2v5M7 4V2h2v5M9 5h2v4l-2 4H5L3 9V7" fill="none" stroke="#4c43a0" stroke-width="1.1"/></svg></span>
    <span class="ic"><svg width="13" height="13" viewBox="0 0 14 14"><path d="M2 1h2v7H2zM5 8l3 5c1 0 1.5-1 1-2.5L8.5 9H12l-1-8H5z" fill="none" stroke="#e02424" stroke-width="1.1"/></svg></span>
    <span class="name">Part-Time Business</span>
    <span class="arrow"></span>
  </div>

  <section class="abs col c1">
    <h3 class="h3">WERQ job description:</h3>
    <p class="desc">Determine and formulate policies and provide overall direction of companies or private and public sector organizations within guidelines set up by a board of directors or similar governing body. Plan, direct, or coordinate operational activities at the highest level of management with the help of subordinate executives and staff managers.</p>
    <a class="btn purple">Learn More About This Job on WERQ</a>
    <a class="btn green">Learn More About This Job on WERQ</a>
  </section>

  <section class="abs col c2">
    <svg class="gauge" width="104" height="54" viewBox="0 0 104 54">
      <path d="M2 52A50 50 0 0 1 12 22L32 37A25 25 0 0 0 27 52z" fill="#e0262b"/>
      <path d="M12 22A50 50 0 0 1 36 5L44 28A25 25 0 0 0 32 37z" fill="#f3892a"/>
      <path d="M36 5A50 50 0 0 1 68 5L60 28A25 25 0 0 0 44 28z" fill="#f6d21e"/>
      <path d="M68 5A50 50 0 0 1 92 22L72 37A25 25 0 0 0 60 28z" fill="#6cc04a"/>
      <path d="M92 22A50 50 0 0 1 102 52H77A25 25 0 0 0 72 37z" fill="#4c43a0"/>
      <line x1="52" y1="50" x2="82" y2="40" stroke="#222" stroke-width="3" stroke-linecap="round"/>
      <circle cx="52" cy="50" r="4" fill="#222"/>
    </svg>
    <p class="match">Your match level (12)</p>
    <h3 class="h3">Average salary</h3>
    <p class="val">$50,000</p>
    <p class="outlook"><i></i>Rising Outlook</p>
    <div class="video" role="img" aria-label="Video about the job: team meeting in an office">
      <svg class="play" width="26" height="26" viewBox="0 0 26 26"><circle cx="13" cy="13" r="12" fill="rgba(255,255,255,.85)"/><path d="M10.5 8.5v9l7-4.5z" fill="#4c43a0"/></svg>
    </div>
    <h3 class="h3 q">Minimum Qualifications</h3>
    <p class="val">None</p>
  </section>

  <section class="abs col c3">
    <h3 class="h3">Top Tips:</h3>
    <ol class="tips">
      <li><b>1.</b><span>You don't need any formal training to become a life coach, but we recommend it.</span></li>
      <li><b>2.</b><span>Life coaching relies on your personal brand so an authentic website is critical for attracting clients. SiteForge is a great place to start.</span></li>
    </ol>
    <h3 class="h3 p">Preferred Online Programs:</h3>
    <div class="prog"><span class="ic"></span><a>Career Learning Works</a></div>
    <div class="prog"><span class="ic"></span><a>Open Commons Institute</a></div>
    <a class="btn green wide">View Part Time Businesses Programs</a>
  </section>

  <div class="abs area">Jobs in their area: <span class="partner"><i></i>Hireloop Finder</span></div>
</main>

<footer class="abs footer">
  <div class="links">News &nbsp;| &nbsp;Privacy Policy &nbsp;| &nbsp;Terms &amp; Conditions &nbsp;| &nbsp;Contact Us</div>
  <div class="copy">Copyright Copper Trail Learning Co © 2021</div>
  <div class="code">C37</div>
</footer>

</body>
</html>
```